Software manual (User manual)

We need a manual for our online e-learning software. Basically what we're looking for is an Adobe InDesign setup (file) where we can add new pages and adjust textual content ourselves.

So the designer would have to come up with an elegant frontpage, page 2,3,4,5 with textual content (some lorem ipsum placeholder text) in a nice setup and a backpage.

We would like the manual to be presented in purple, specifically the purple being used in our logo (maybe cover the enitre front and backpage in purple) which is our main color (together with grey), at least for front- and back-page.

The design should be simple and elegant. Myriad-Pro Light is the font we'd like to see in headings while maybe something like Helvetica being used for the bulk text.

Industry/Entity Type

Software

Requirements
Must have
• The manual must have our logo in either colors or white depending on your choice of setup. See attached colored logo. We accept changing logo colors to all white.

It should include our email on the backpage together with the company name.

The text "User manual" should be present on the frontpage.

Either the front or backpage should have the text "edition" or "version" with a number or something similar so it's easier for users to distinguish the old manuals from the new ones.

The size should be A4

Should include an index, preferbly set up so that is updates automatically if pages are added/removed.

Each page should be numbered, aside from front and back.

As this is a user manual we do not want images. Vector graphics are ok.

"Less is more"

```html
<!DOCTYPE html>
<html lang="en">
<head>
<meta charset="utf-8">
<title>User Manual V1.0 – Index</title>
<link rel="stylesheet" href="https://fonts.googleapis.com/css2?family=Open+Sans:wght@300;400;600;700&display=swap">
<style>
  :root {
    --purple-deep: #2b1733;
    --purple: #5e2468;
    --grey: #939598;
    --grey-light: #e6e6e6;
    --ink: #111111;
    --page-num: #4a4a4a;
    --white: #ffffff;
  }
  html, body { margin: 0; padding: 0; overflow: hidden; background: var(--white); }
  .page {
    position: relative;
    width: 848px; height: 1200px;
    overflow: hidden;
    background: var(--white);
    font-family: "Open Sans", Arial, sans-serif;
  }
  .side-band { position: absolute; left: 0; top: 0; }
  .manual-label {
    position: absolute; left: 11px; top: 78px;
    color: var(--white); font-weight: 300;
    font-size: 28px; line-height: 34px; letter-spacing: 0.5px;
    margin: 0;
  }
  .version-mark {
    position: absolute; left: 9px; top: 140px;
    color: var(--white); font-weight: 300; margin: 0;
    line-height: 1;
  }
  .version-mark .v { font-size: 72px; }
  .version-mark .num { font-size: 38px; }
  .brand {
    position: absolute; left: 16px; top: 1112px;
    color: var(--white); font-weight: 600; font-size: 34px;
    margin: 0; letter-spacing: 0.5px;
  }
  .index-title {
    position: absolute; left: 380px; top: 166px;
    margin: 0; font-weight: 300; font-size: 64px;
    color: var(--ink); letter-spacing: 1px; line-height: 1;
  }
  .index-panel { position: absolute; left: 0; top: 0; }
  .page-strip {
    position: absolute; left: 577px; top: 285px;
    width: 37px; height: 740px; background: var(--grey-light);
  }
  .index-list { list-style: none; margin: 0; padding: 0; }
  .index-letter, .index-entry, .index-page { position: absolute; margin: 0; }
  .index-letter {
    left: 381px; color: var(--white); font-weight: 700; font-size: 22px; line-height: 1;
  }
  .index-entry {
    left: 381px; color: var(--white); font-weight: 400; font-size: 11.5px;
    line-height: 1; letter-spacing: -0.1px;
  }
  .index-page {
    left: 585px; color: var(--page-num); font-size: 12px; line-height: 1;
  }
</style>
</head>
<body>
<div class="page">
  <svg class="side-band" width="848" height="1200" viewBox="0 0 848 1200" aria-hidden="true">
    <defs>
      <linearGradient id="bandFill" x1="0" y1="0" x2="1" y2="0">
        <stop offset="0" stop-color="var(--purple-deep)" style="stop-color:#2b1733"/>
        <stop offset="0.6" stop-color="#5e2468"/>
      </linearGradient>
    </defs>
    <polygon points="0,0 117,0 181,1200 0,1200" fill="url(#bandFill)"/>
  </svg>

  <p class="manual-label">USER<br>MANUAL</p>
  <p class="version-mark"><span class="v">V</span><span class="num">1.0</span></p>
  <p class="brand">Coursely</p>

  <h1 class="index-title">INDEX</h1>

  <svg class="index-panel" width="848" height="1200" viewBox="0 0 848 1200" aria-hidden="true">
    <polygon points="318,251 571,251 571,1045 362,1045" fill="#939598"/>
  </svg>
  <div class="page-strip"></div>

  <ul class="index-list">
    <li>
      <h2 class="index-letter" style="top:278px">G</h2>
      <span class="index-entry" style="top:313px">GRAPHICS</span>
      <span class="index-page" style="top:313px">5</span>
    </li>
    <li>
      <h2 class="index-letter" style="top:346px">H</h2>
      <span class="index-entry" style="top:392px">HELP</span>
      <span class="index-page" style="top:392px">6</span>
    </li>
    <li>
      <h2 class="index-letter" style="top:434px">I</h2>
      <span class="index-entry" style="top:470px">INTRODUCTION</span>
      <span class="index-page" style="top:470px">3</span>
    </li>
    <li>
      <h2 class="index-letter" style="top:501px">S</h2>
      <span class="index-entry" style="top:538px">STATISTIC</span>
      <span class="index-page" style="top:538px">4</span>
    </li>
    <li>
      <h2 class="index-letter" style="top:570px">V</h2>
      <span class="index-entry" style="top:607px">VERSION 1.0</span>
      <span class="index-page" style="top:607px">2</span>
    </li>
    <li>
      <h2 class="index-letter" style="top:637px">W</h2>
      <span class="index-entry" style="top:675px">WHAT WILL THE SOFTWARE DO?</span>
      <span class="index-page" style="top:675px">3</span>
    </li>
  </ul>
</div>
</body>
</html>
```